Facebook and Instagram advertisment

Create a advertisement for Facebook and Instagram
Text:
Introducing BRISK
Speeds to 500 Mbps
Packages start at only $89.99 monthly for speeds to 100Mbps
Check out our Bramley for the Holidays Event, FREE Equipment, FREE Installation, FREE wifi6 router and first month of service FREE!

```html
<!DOCTYPE html>
<html lang="en">
<head>
<meta charset="UTF-8">
<title>Introducing BRISK – Bramley Satellite</title>
<link rel="stylesheet" href="https://fonts.googleapis.com/css2?family=Poppins:wght@300;400;600;700;800&display=swap">
<style>
  :root {
    --navy-deep: #07093f;
    --navy: #0b0f8a;
    --royal: #1b2fd6;
    --cyan: #2ee6f4;
    --green: #4fe07f;
    --white: #ffffff;
  }
  * { margin: 0; padding: 0; box-sizing: border-box; }
  html, body {
    width: 1200px; height: 1200px; overflow: hidden;
    background: var(--navy-deep);
  }
  .ad {
    position: relative; width: 1200px; height: 1200px; overflow: hidden;
    font-family: "Poppins", sans-serif; color: var(--white);
  }
  .ad__backdrop { position: absolute; inset: 0; }
  .ad__text { position: absolute; left: 0; width: 100%; text-align: center; white-space: nowrap; }
  .intro { top: 128px; font-size: 40px; line-height: 50px; font-weight: 400; letter-spacing: 8px; }
  .product-name {
    top: 170px; font-size: 150px; font-weight: 800; line-height: 1;
    color: var(--cyan); letter-spacing: 2px;
  }
  .headline { top: 360px; font-size: 70px; line-height: 84px; font-weight: 300; }
  .headline strong { font-weight: 700; }
  .price-line { top: 482px; font-size: 32px; line-height: 70px; font-weight: 400; }
  .price-line strong { font-size: 64px; font-weight: 700; vertical-align: -4px; }
  .price-note { top: 546px; font-size: 30px; line-height: 40px; font-weight: 400; }
  .price-note strong { font-weight: 700; }
  .event-title { top: 694px; font-size: 40px; font-weight: 300; line-height: 43px; }
  .perks { position: absolute; left: 388px; top: 798px; list-style: none; }
  .perk { display: flex; align-items: flex-start; height: 49px; line-height: 46px; }
  .perk__tick { width: 28px; height: 46px; margin-right: 12px; flex: none; }
  .perk__free { width: 138px; font-size: 44px; font-weight: 700; color: var(--green); flex: none; }
  .perk__item { font-size: 43px; font-weight: 400; line-height: 35px; padding-top: 6px; }
  .brand-plate {
    position: absolute; left: 372px; top: 1078px; width: 456px; height: 260px;
    background: var(--white); border-radius: 50%;
  }
  .brand {
    position: absolute; left: 0; width: 100%; top: 1134px;
    text-align: center; font-size: 32px; line-height: 40px; font-weight: 600; color: var(--navy);
  }
</style>
</head>
<body>
<main class="ad">
  <svg class="ad__backdrop" viewBox="0 0 1200 1200" role="img" aria-label="Abstract flowing blue and violet waves on deep navy">
    <defs>
      <linearGradient id="sky" x1="0" y1="0" x2="1" y2="1">
        <stop offset="0" stop-color="#1f3fe0"/>
        <stop offset="0.45" stop-color="#141aa8"/>
        <stop offset="1" stop-color="#07093f"/>
      </linearGradient>
      <linearGradient id="violetWave" x1="0" y1="0" x2="1" y2="0">
        <stop offset="0" stop-color="#8a3cf2"/>
        <stop offset="1" stop-color="#3b3fe0"/>
      </linearGradient>
      <linearGradient id="lightWave" x1="0" y1="0" x2="1" y2="1">
        <stop offset="0" stop-color="#3e4fe6"/>
        <stop offset="0.7" stop-color="#8a90f0"/>
        <stop offset="1" stop-color="#d4d0fa"/>
      </linearGradient>
      <radialGradient id="lowerField" cx="0.5" cy="0.1" r="0.9">
        <stop offset="0" stop-color="#0d1aa8"/>
        <stop offset="1" stop-color="#0a0f78"/>
      </radialGradient>
    </defs>
    <rect width="1200" height="1200" fill="url(#sky)"/>
    <path d="M560 0 C 700 120, 520 260, 720 360 C 900 450, 1100 300, 1200 340 L1200 0 Z" fill="#07093f" opacity="0.85"/>
    <path d="M0 300 C 120 240, 300 260, 340 380 C 380 500, 300 640, 0 700 Z" fill="url(#violetWave)" opacity="0.9"/>
    <path d="M540 560 C 700 430, 900 340, 1200 300 L1200 640 C 1000 600, 760 600, 540 560 Z" fill="url(#lightWave)" opacity="0.85"/>
    <path d="M0 720 C 300 590, 900 590, 1200 700 L1200 1200 L0 1200 Z" fill="url(#lowerField)"/>
  </svg>

  <p class="ad__text intro">INTRODUCING</p>
  <h1 class="ad__text product-name">BRISK</h1>
  <p class="ad__text headline">Speeds to <strong>500 Mbps</strong></p>
  <p class="ad__text price-line">Packages start at only <strong>$89.99 monthly</strong></p>
  <p class="ad__text price-note">for speeds to <strong>100Mbps</strong></p>
  <p class="ad__text event-title">Check out our Bramley<br>for the Holidays Event</p>

  <ul class="perks">
    <li class="perk">
      <svg class="perk__tick" viewBox="0 0 28 46"><path d="M3 25 L11 33 L25 18" fill="none" stroke="var(--green)" stroke-width="4.5" stroke-linecap="round" stroke-linejoin="round"/></svg>
      <span class="perk__free">FREE</span><span class="perk__item">Equipment</span>
    </li>
    <li class="perk">
      <svg class="perk__tick" viewBox="0 0 28 46"><path d="M3 25 L11 33 L25 18" fill="none" stroke="var(--green)" stroke-width="4.5" stroke-linecap="round" stroke-linejoin="round"/></svg>
      <span class="perk__free">FREE</span><span class="perk__item">Installation</span>
    </li>
    <li class="perk">
      <svg class="perk__tick" viewBox="0 0 28 46"><path d="M3 25 L11 33 L25 18" fill="none" stroke="var(--green)" stroke-width="4.5" stroke-linecap="round" stroke-linejoin="round"/></svg>
      <span class="perk__free">FREE</span><span class="perk__item">Wifi6 router</span>
    </li>
    <li class="perk">
      <svg class="perk__tick" viewBox="0 0 28 46"><path d="M3 25 L11 33 L25 18" fill="none" stroke="var(--green)" stroke-width="4.5" stroke-linecap="round" stroke-linejoin="round"/></svg>
      <span class="perk__free">FREE</span><span class="perk__item">First month<br>of service</span>
    </li>
  </ul>

  <div class="brand-plate"></div>
  <p class="brand">Bramley Satellite</p>
</main>
</body>
</html>
```